Cafe menu design

Hi there,

We need a editable menu layout and design to match our new cafe call: " Larkspur Fine Coffee", we love the ideas of A4 clip board and self print out menu in black and white. ( Example as attached)

We would like the menu can be break down into category easy for customer to flip around and read. ( example as attached)

Category including the following:

- All day breakfast and Sandwich and Toast
- Main (Lunch&Dinner) and Pizza
- Dessert snacks and nibbles
- Hot and Cold Drinks
- Catering menu

Please find our logo and our current menu as attached for your information and convenience.
Updates

Dear Designers, Thank you for your time and submission, Please find our drink menu and logo as attached. Kind Regards,

Target Market(s)

Young family, young Couple, office and corporate staff

Industry/Entity Type

Cafe

Font styles to use
Serif
Sans Serif

```html
<!DOCTYPE html>
<html lang="en">
<head>
<meta charset="utf-8">
<title>Larkspur Fine Coffee – All Day Breakfast Menu</title>
<link rel="stylesheet" href="https://fonts.googleapis.com/css2?family=Montserrat:wght@400;600;700;800&family=Lora:wght@400;600&display=swap">
<style>
  :root{
    --bg:#d9d8d4;
    --paper:#f4f4f2;
    --ink:#141414;
    --ink-soft:#4a4a4a;
    --rule:#bdbdbb;
    --tab:#e4e4e2;
  }
  *{box-sizing:border-box;margin:0;padding:0}
  html,body{width:1200px;height:794px;overflow:hidden;background:var(--bg)}
  body{font-family:"Montserrat",Arial,sans-serif;color:var(--ink);position:relative}

  .menu-page{
    position:absolute;left:330px;top:17px;width:540px;height:760px;
    background:var(--paper);box-shadow:0 2px 10px rgba(0,0,0,.18);overflow:hidden;
  }
  .brand-corner{
    position:absolute;right:0;top:0;width:200px;height:112px;
    background:var(--ink);border-bottom-left-radius:120px 112px;
    display:flex;align-items:center;justify-content:flex-end;padding-right:24px;gap:8px;
  }
  .brand-mark{width:10px;height:10px;border-radius:50%;background:var(--paper)}
  .brand-name{
    color:var(--paper);font-weight:700;font-size:13px;letter-spacing:.14em;
    text-transform:uppercase;line-height:1.35;text-align:center;width:110px;
  }
  .leaf-ornament{position:absolute;left:30px;top:100px;width:86px;height:26px;
    background:linear-gradient(90deg,#222,#555);border-radius:13px 2px 13px 2px}

  .section-head{position:absolute;left:30px;top:138px;right:30px}
  .section-title{font-weight:800;font-size:15px;letter-spacing:-.01em}
  .section-note{font-family:"Lora",Georgia,serif;font-size:8.5px;color:var(--ink-soft);margin-top:3px}

  .columns{position:absolute;left:30px;right:30px;top:186px;display:flex;gap:34px}
  .column{flex:1;display:flex;flex-direction:column;gap:14px}

  .item{display:flex;justify-content:space-between;align-items:flex-start;gap:10px}
  .item-name{font-weight:700;font-size:11px;line-height:1.25}
  .item-desc{font-family:"Lora",Georgia,serif;font-size:8.5px;color:var(--ink-soft);margin-top:2px;line-height:1.3}
  .item-price{font-weight:600;font-size:10.5px;white-space:nowrap}

  .extras{list-style:none;margin-top:4px;font-size:8.5px;color:var(--ink-soft);width:120px}
  .extras li{display:flex;justify-content:space-between;line-height:1.45}
  .extras li::before{content:"–";margin-right:5px}
  .extras li span:first-child{flex:1}

  .page-foot{position:absolute;left:30px;right:30px;bottom:44px;border-top:1px solid var(--rule)}
  .next-tab{
    position:absolute;right:0;bottom:0;width:120px;height:44px;background:var(--tab);
    border-left:1px solid var(--rule);border-top:1px solid var(--rule);
    display:flex;align-items:center;justify-content:center;
    font-weight:700;font-size:11px;letter-spacing:.18em;color:#8a8a88;
  }
</style>
</head>
<body>
<main class="menu-page">
  <header class="brand-corner">
    <span class="brand-mark"></span>
    <span class="brand-name">Larkspur Fine Coffee</span>
  </header>
  <div class="leaf-ornament" role="img" aria-label="Decorative leaf sprig"></div>

  <div class="section-head">
    <h1 class="section-title">All day breakfast &amp; Sandwich and Toast</h1>
    <p class="section-note">Served from 7am until close, ask staff about gluten free options</p>
  </div>

  <div class="columns">
    <section class="column">
      <div class="item"><div><p class="item-name">Sourdough toast</p><p class="item-desc">Butter and jam on the side</p></div><span class="item-price">4</span></div>
      <div class="item"><div><p class="item-name">Toasted fruit loaf with butter</p></div><span class="item-price">6</span></div>
      <div class="item"><div><p class="item-name">Pancake</p><p class="item-desc">with maple syrup, berries &amp; cream</p></div><span class="item-price">12</span></div>
      <div class="item"><div><p class="item-name">Poppy seed / blueberry bagel</p><p class="item-desc">with cream cheese</p></div><span class="item-price">6</span></div>
      <div class="item"><div><p class="item-name">Poppy seed bagel</p><p class="item-desc">smoked salmon, capers &amp; cream cheese</p></div><span class="item-price">12</span></div>
      <div class="item"><div><p class="item-name">Low fat Greek yoghurt</p><p class="item-desc">with honey, granola &amp; fresh berries</p></div><span class="item-price">8</span></div>
      <div class="item"><div><p class="item-name">Smoked ham &amp; tasty cheese croissant</p></div><span class="item-price">8.5</span></div>
      <div class="item"><div><p class="item-name">Tasty cheese &amp; tomato croissant</p></div><span class="item-price">7</span></div>
      <div class="item"><div><p class="item-name">Date Scone</p><p class="item-desc">with butter &amp; jam</p></div><span class="item-price">4.5</span></div>
      <div class="item"><div><p class="item-name">Half sourdough sandwiches</p><p class="item-desc">Choose ham, chicken or egg salad</p></div><span class="item-price">9</span></div>
    </section>

    <section class="column">
      <div class="item"><div><p class="item-name">Fresh brown, grilled haloumi</p><p class="item-desc">Wilted spinach, tomato &amp; sourdough toast</p></div><span class="item-price">16</span></div>
      <div class="item"><div><p class="item-name">Breakfast with Eggs</p><p class="item-desc">Two eggs your way on sourdough with butter</p>
        <ul class="extras">
          <li><span>Bacon</span><span>4</span></li>
          <li><span>Avocado</span><span>3.5</span></li>
          <li><span>Mushroom</span><span>3</span></li>
          <li><span>Tomato</span><span>2.5</span></li>
          <li><span>Hash brown</span><span>2.5</span></li>
        </ul></div><span class="item-price">10</span></div>
      <div class="item"><div><p class="item-name">Bacon &amp; eggs panini</p><p class="item-desc">with tasty cheese &amp; tomato relish</p></div><span class="item-price">10</span></div>
      <div class="item"><div><p class="item-name">Double bacon, egg &amp; hash brown roll</p><p class="item-desc">with BBQ sauce</p></div><span class="item-price">12</span></div>
      <div class="item"><div><p class="item-name">Tropical omelette</p><p class="item-desc">ham, pineapple, cheese &amp; spring onion</p></div><span class="item-price">15</span></div>
      <div class="item"><div><p class="item-name">Eggs benedict</p><p class="item-desc">poached eggs, ham or salmon, hollandaise on toasted muffin</p></div><span class="item-price">17</span></div>
      <div class="item"><div><p class="item-name">Larkspur well-being brekky</p><p class="item-desc">poached eggs, avocado, spinach, tomato, mushroom &amp; grain toast</p></div><span class="item-price">19</span></div>
      <div class="item"><div><p class="item-name">Larkspur mighty brekky</p><p class="item-desc">eggs, bacon, sausage, hash brown, beans &amp; toast</p></div><span class="item-price">22</span></div>
    </section>
  </div>

  <div class="page-foot"></div>
  <div class="next-tab">DRINKS</div>
</main>
</body>
</html>
```